Mr Pellowes Yard Works flyer for newsletter

I need a professional looking flyer design for my company Mr Pellowes Yard Works based in New Braunfels, TX to boost sales. Must include the following: Lawn service starting at $40 (mowing, edging, leaf blowing) Tree trimming starting at $125. Other services-mulching, shrub trimming, aeration, flower bed maintenance, Fall/spring clean up. Serving New Braunfels and surrounding areas. To set up and estimate please call 512 555 0143 or email mrpellowesyard@example-mail.net

Industry/Entity Type

Landscaping

Font styles to use
Serif

Colors

Designer to choose colors to be used in the design.

Requirements
Must have
• Phone number 512 555 0143
• Email mrpellowesyard@example-mail.net

```html
<!DOCTYPE html>
<html lang="en">
<head>
<meta charset="utf-8">
<title>Mr Pellowes Yard Works – Flyer</title>
<link href="https://fonts.googleapis.com/css2?family=Barlow:wght@200&family=Barlow+Condensed:wght@400;500;600;700&display=swap" rel="stylesheet">
<style>
  :root {
    --red: #d8222d;
    --lime: #c4cf22;
    --white: #ffffff;
    --ink: #1b1b1b;
    --stage: #ebe8e3;
    --grass-dark: #6a9636;
    --grass-light: #a8c274;
  }
  * { margin: 0; padding: 0; box-sizing: border-box; }
  html, body { width: 1200px; height: 1200px; overflow: hidden; }
  body { background: var(--stage); position: relative; font-family: "Barlow Condensed", sans-serif; }

  .flyer {
    position: absolute; left: 170px; top: 44px;
    width: 860px; height: 1112px; overflow: hidden;
    background: var(--white);
    box-shadow: 0 6px 22px rgba(0,0,0,.18);
  }
  .hero-photo {
    position: absolute; left: 0; top: 299px; width: 860px; height: 813px;
    background: linear-gradient(180deg, #f6f6f4 0%, #e3e8d9 28%, #c9a7a1 52%, var(--grass-light) 70%, var(--grass-dark) 100%);
  }
  .shapes { position: absolute; inset: 0; }

  .brand-mark {
    position: absolute; left: 22px; top: 230px;
    font-family: "Barlow Condensed", sans-serif; font-weight: 600;
    font-size: 26px; color: var(--white); letter-spacing: 1px;
    transform-origin: left top;
  }
  .title-top {
    position: absolute; left: 158px; top: 18px;
    font-family: "Barlow", sans-serif; font-weight: 200;
    font-size: 116px; line-height: 1; color: var(--white); letter-spacing: -1px;
  }
  .title-bottom {
    position: absolute; right: 30px; top: 136px;
    font-weight: 700; font-size: 128px; line-height: 1; color: var(--lime);
  }

  .price-box {
    position: absolute; top: 299px; height: 255px;
    background: rgba(255,255,255,.86);
    border: 6px solid var(--lime); border-top: none;
    text-align: center; color: var(--ink);
  }
  .price-box.lawn { left: 195px; width: 276px; }
  .price-box.tree { left: 525px; width: 273px; }
  .box-title { color: var(--red); font-weight: 700; font-size: 46px; line-height: .98; margin-top: 18px; }
  .box-note { font-weight: 400; font-size: 18px; margin-top: 6px; }
  .box-start { font-weight: 500; font-size: 27px; margin-top: 6px; }
  .price-box.tree .box-start { margin-top: 16px; }
  .box-price { color: var(--red); font-weight: 600; font-size: 68px; line-height: 1; }
  .box-price sup { font-size: 40px; vertical-align: -4px; margin-right: 2px; }

  .other-services {
    position: absolute; left: 195px; top: 580px; width: 680px; height: 275px;
    background: rgba(255,255,255,.5);
    border: 6px solid var(--lime); border-right: none;
  }
  .other-title {
    position: absolute; left: 34px; top: 18px;
    color: var(--red); font-weight: 700; font-size: 38px; letter-spacing: .5px; word-spacing: 6px;
  }
  .service-list { position: absolute; list-style: none; font-weight: 600; font-size: 27px; color: var(--ink); line-height: 1.12; }
  .service-list.left { left: 34px; top: 76px; }
  .service-list.right { left: 360px; top: 76px; }
  .service-list li { margin-bottom: 20px; }
  .service-list.right li { margin-bottom: 20px; }

  .contact { position: absolute; left: 32px; top: 912px; }
  .contact-lead { color: var(--white); font-weight: 600; font-size: 42px; line-height: 1; }
  .contact-phone {
    display: flex; align-items: center; gap: 14px; margin-top: 10px;
    color: var(--lime); font-weight: 600; font-size: 72px; line-height: 1;
  }
  .contact-email {
    display: flex; align-items: center; gap: 16px; margin-top: 10px;
    color: var(--lime); font-weight: 500; font-size: 29px; line-height: 1;
  }

  .service-area {
    position: absolute; right: 18px; top: 900px; text-align: right; color: var(--red);
  }
  .service-area-title { font-weight: 700; font-size: 32px; letter-spacing: 9px; line-height: 1; margin-right: -9px; }
  .service-area-place { font-weight: 500; font-size: 23px; line-height: 1.3; margin-top: 6px; }
</style>
</head>
<body>
  <main class="flyer">
    <div class="hero-photo" role="img" aria-label="Photo of a red push lawn mower on a green lawn with yellow wildflowers, faded to white at the top, with red line drawings of garden tools"></div>

    <svg class="shapes" width="860" height="1112" viewBox="0 0 860 1112" aria-hidden="true">
      <rect class="header-band" x="0" y="0" width="860" height="299" fill="var(--red)"/>
      <polygon class="corner-wedge" points="0,0 64,0 260,299 195,299 0,469" fill="var(--lime)"/>
      <polygon class="contact-panel" points="0,881 450,881 610,1112 0,1112" fill="var(--red)"/>
      <polygon class="area-panel" points="553,881 860,881 860,1020 651,1020" fill="var(--lime)"/>
    </svg>

    <div class="brand-mark">Mr Pellowes</div>

    <h1 class="title">
      <span class="title-top">Mr Pellowes</span>
      <span class="title-bottom">Yard Works</span>
    </h1>

    <section class="price-box lawn">
      <h2 class="box-title">LAWN<br>SERVICE</h2>
      <p class="box-note">MOWING, EDGING, LEAF BLOWING</p>
      <p class="box-start">STARTING AT</p>
      <p class="box-price"><sup>$</sup>40</p>
    </section>

    <section class="price-box tree">
      <h2 class="box-title">TREE<br>TRIMMING</h2>
      <p class="box-start">STARTING AT</p>
      <p class="box-price"><sup>$</sup>125</p>
    </section>

    <section class="other-services">
      <h2 class="other-title">OTHER SERVICES</h2>
      <ul class="service-list left">
        <li>MULCHING</li>
        <li>SHRUB TRIMMING</li>
        <li>AERATION</li>
      </ul>
      <ul class="service-list right">
        <li>FLOWER BED<br>MAINTENANCE</li>
        <li>FALL/SPRING<br>CLEAN UP</li>
      </ul>
    </section>

    <section class="contact">
      <p class="contact-lead">TO SET UP &amp; ESTIMATE</p>
      <p class="contact-phone">
        <svg width="30" height="56" viewBox="0 0 30 56" aria-hidden="true">
          <path d="M14 2 L22 4 L19 16 L12 17 C10 25 10 32 12 39 L19 40 L22 52 L14 54 C4 46 1 35 2 27 C3 17 7 8 14 2 Z" fill="var(--lime)"/>
        </svg>
        512 555 0143
      </p>
      <p class="contact-email">
        <svg width="32" height="22" viewBox="0 0 32 22" aria-hidden="true">
          <rect x="1.5" y="1.5" width="29" height="19" fill="none" stroke="var(--lime)" stroke-width="3"/>
          <polyline points="2,2 16,13 30,2" fill="none" stroke="var(--lime)" stroke-width="3"/>
        </svg>
        mrpellowesyard@example-mail.net
      </p>
    </section>

    <section class="service-area">
      <p class="service-area-title">SERVING</p>
      <p class="service-area-place">NEW BRAUNFELS &amp;<br>SURROUNDING AREAS</p>
    </section>
  </main>
</body>
</html>
```